Brenmoor Group needs a business card

I would like the card to be simple but modern and elegant.
I like black and white.
or black and gold.
we are a private finance lender and also are involved in property and property developments.

please look at the business card photos i provided i would like B.G only one one side and all the other details on the other side use fonts that tie in with my theme.

Industry/Entity Type

Finance

Contact Information for Business Card

Brenmoor Group (B.G) Callum Brenmoor M: 0418396152 E: callumbren@quivomail.com

Font styles to use
Other font styles liked:
• Use fonts that would reflect our business

Colors
000000
ffffff

Requirements
Must have
• one side of details
• other side has either B.G or Brenmoor Group like in the photos provided

```html
<!DOCTYPE html>
<html lang="en">
<head>
<meta charset="utf-8">
<title>Brenmoor Group — Business Card</title>
<link rel="stylesheet" href="https://fonts.googleapis.com/css2?family=Playfair+Display:wght@400;700;900&display=swap">
<style>
  :root {
    --ink: #000000;
    --paper: #ffffff;
  }
  * { margin: 0; padding: 0; box-sizing: border-box; }
  html, body {
    width: 942px;
    height: 1200px;
    overflow: hidden;
    background: var(--paper);
  }
  .sheet {
    position: relative;
    width: 942px;
    height: 1200px;
    background: var(--paper);
    font-family: "Playfair Display", Georgia, serif;
    color: var(--ink);
  }
  .card {
    position: absolute;
    left: 83px;
    width: 780px;
    height: 505px;
  }
  .card--front {
    top: 77px;
    background: var(--ink);
    display: flex;
    align-items: center;
    justify-content: center;
  }
  .card--back {
    top: 621px;
    background: var(--paper);
    border: 2px solid var(--ink);
    text-align: center;
  }
  .monogram {
    font-weight: 900;
    line-height: 1;
    letter-spacing: -2px;
  }
  .card--front .monogram {
    color: var(--paper);
    font-size: 186px;
    margin-top: -14px;
  }
  .card--back .monogram {
    position: absolute;
    left: 0; right: 0;
    top: 100px;
    font-size: 86px;
    color: var(--ink);
  }
  .company-name {
    position: absolute;
    left: 0; right: 0;
    top: 188px;
    font-size: 40px;
    font-weight: 700;
    line-height: 1.2;
  }
  .contact {
    position: absolute;
    left: 0; right: 0;
    top: 292px;
    line-height: 1;
  }
  .contact__name {
    font-size: 28px;
    font-weight: 400;
    margin-bottom: 22px;
  }
  .contact__phone {
    font-size: 23px;
    margin-bottom: 6px;
  }
  .contact__email {
    font-size: 21px;
  }
</style>
</head>
<body>
  <main class="sheet">
    <section class="card card--front" aria-label="Card front">
      <div class="monogram">BG</div>
    </section>

    <section class="card card--back" aria-label="Card back">
      <div class="monogram">BG</div>
      <h1 class="company-name">Brenmoor Group</h1>
      <div class="contact">
        <p class="contact__name">Callum Brenmoor</p>
        <p class="contact__phone">0418396152</p>
        <p class="contact__email">callumbren@quivomail.com</p>
      </div>
    </section>
  </main>
</body>
</html>
```